Brindle Grass Services website design

We want to create a Sports turf website for our business Brindle Grass Services - we do sports turf management on sports fields around the Mackay region soccer rugby league softball fields etc from full turf management plans and maintenance to just supply and apply of turf management products and just supply of products with program we also do grounds facility maintenance at council facility's and grounds that require a higher level of care - we will up load our logos and fonts etc to assist with the colour pallet for the website - we will have to have a landing page a shop page with tabs a gallery tab along with a grants initiative and our coastals finest green tab also - our font for the txt is called ethnocentric
Updates

how do we open time for people to submit we have no one submitted

Industry/Entity Type

Turf

Coding

Coded - Design and coding required

Number of Pages Required

5+ page

Font styles to use
Other font styles liked:
• ethnocentric

Requirements
Must have
• I have mentioned some waffle in the description that should assist
Should not have
• anything not related

```html
<!DOCTYPE html>
<html lang="en">
<head>
<meta charset="utf-8">
<title>Brindle Grass Services</title>
<link href="https://fonts.googleapis.com/css2?family=Michroma&family=Montserrat:wght@400;500;600;700&display=swap" rel="stylesheet">
<style>
:root{
  --black:#000;
  --white:#fff;
  --lime:#6fb83f;
  --green:#3f9a3a;
  --forest:#0a6b35;
  --deep:#1f5a26;
  --ink:#111;
  --text:#3a3a3a;
  --card:#f4f4f4;
  --muted:#b0b0b0;
}
*{margin:0;padding:0;box-sizing:border-box}
html,body{width:1200px;height:2260px;overflow:hidden;background:var(--white)}
body{position:relative;font-family:"Montserrat",sans-serif;color:var(--text)}
.abs{position:absolute}
.display{font-family:"Michroma",sans-serif;text-transform:uppercase;color:var(--ink);line-height:1}

/* header */
.site-header{left:0;top:0;width:1200px;height:82px;background:var(--black);z-index:5}
.brand{left:139px;top:28px;display:flex;align-items:center;gap:8px;color:var(--white);font-weight:700;font-size:17px;letter-spacing:.5px}
.brand-dot{width:12px;height:12px;border-radius:50%;background:var(--lime)}
.nav{right:348px;top:33px;display:flex;gap:14px;font-size:13px;color:var(--white);white-space:nowrap}
.search{left:877px;top:30px}
.btn-contact{left:911px;top:25px;width:121px;height:33px;border-radius:17px;background:var(--lime);color:var(--white);font-size:13px;display:flex;align-items:center;justify-content:center}
.bag{left:1051px;top:30px}

/* hero */
.hero{left:0;top:82px;width:1200px;height:650px}
.hero-photo{left:0;top:82px;width:1200px;height:650px;background:linear-gradient(180deg,#2c3a3f 0%,#3d4a48 40%,#3f7a2d 55%,#4e9a32 80%,#5aa83a 100%);clip-path:polygon(0 0,100% 0,100% 90%,0 99%)}
.hero-title{left:158px;top:236px;font-size:47px;color:var(--white);line-height:62px}
.hero-copy{left:158px;top:366px;width:520px;font-size:16px;line-height:24px;color:var(--white)}
.btn-dark{background:var(--black);color:var(--white);border-radius:18px;font-size:13px;display:flex;align-items:center;justify-content:center}
.hero-btn{left:158px;top:466px;width:143px;height:35px}
.badge-text{left:952px;top:426px;width:140px;text-align:center;color:var(--white);font-size:20px;line-height:24px}
.badge-text b{font-weight:700}
.dots{left:1078px;top:653px;display:flex;gap:5px}
.dots span{width:18px;height:3px;background:var(--white);border-radius:2px}
.dots span:first-child{background:var(--black)}

/* about */
.about-frame{left:106px;top:1038px;width:440px;height:345px;border-radius:14px;background:linear-gradient(90deg,var(--lime),var(--forest))}
.about-photo{left:140px;top:849px;width:430px;height:498px;border-radius:12px;background:linear-gradient(180deg,#cfe3f2 0%,#9cc4de 35%,#4a8fb0 48%,#5c9a34 60%,#2f6a1d 100%)}
.about-square{left:507px;top:833px;width:72px;height:71px;border-radius:5px;background:var(--lime)}
.turf-roll{left:377px;top:1201px;width:215px;height:210px;border-radius:40px 40px 30px 30px;background:linear-gradient(160deg,#5aa832,#2f7a1c)}
.about-title{left:651px;top:903px;font-size:36px}
.about-copy{left:651px;top:961px;width:405px;font-size:13px;line-height:21px}
.checks{left:651px;top:1079px;width:410px;list-style:none}
.checks li{display:flex;gap:8px;font-size:13px;line-height:21px;margin-bottom:21px}
.checks li:nth-child(2){margin-bottom:26px}
.checks svg{flex:none;margin-top:2px}
.checks b{color:#222;font-weight:700}
.about-btn{left:651px;top:1291px;width:129px;height:34px}

/* responsibilities */
.key-title{left:0;top:1546px;width:1200px;text-align:center;font-size:36px}
.card{top:1640px;width:274px;height:326px;background:var(--card);border-radius:6px;padding:54px 30px 0}
.card-icon{width:62px;height:62px;border-radius:50%;background:linear-gradient(135deg,var(--green),var(--forest));display:flex;align-items:center;justify-content:center}
.card h3{margin-top:20px;font-size:17.5px;line-height:24px;font-weight:700;color:var(--ink)}
.card p{margin-top:12px;font-size:13.5px;line-height:21px}
.more{margin-top:16px;display:flex;align-items:center;gap:7px;font-weight:700;font-size:13.5px;color:var(--ink)}
.more-dot{width:19px;height:19px;border-radius:50%;background:var(--green);display:flex;align-items:center;justify-content:center}
.progress{left:0;top:2145px;width:1200px;text-align:center;font-size:38px;color:var(--muted)}
</style>
</head>
<body>

<header class="abs site-header">
  <div class="abs brand"><span class="brand-dot"></span>Brindle Grass Services</div>
  <nav class="abs nav"><span>Home</span><span>About us</span><span>Gallery</span><span>Grants</span><span>Finest green</span></nav>
  <svg class="abs search" width="22" height="22" viewBox="0 0 22 22" fill="none" stroke="#fff" stroke-width="1.6"><circle cx="9.5" cy="9.5" r="8"/><path d="M15.5 15.5l5 5"/></svg>
  <div class="abs btn-contact">Contact</div>
  <svg class="abs bag" width="22" height="24" viewBox="0 0 22 24"><path d="M3 8h14v13H3z" fill="#fff"/><path d="M7 8V5a3 3 0 0 1 6 0v3" fill="none" stroke="#fff" stroke-width="1.6"/><circle cx="17" cy="4" r="3.5" fill="#6fb83f"/></svg>
</header>

<div class="abs hero-photo" role="img" aria-label="Floodlit stadium with a freshly mown sports field"></div>
<svg class="abs hero" viewBox="0 0 1200 650" width="1200" height="650">
  <defs>
    <linearGradient id="heroGreen" x1="0" y1="0" x2="1" y2="1">
      <stop offset="0" stop-color="#72b840"/><stop offset="1" stop-color="#2f8a3a"/>
    </linearGradient>
  </defs>
  <path d="M0 0H652L492 295Q446 370 480 430L596 620L0 646Z" fill="#1f5a26"/>
  <path d="M0 0H620L462 295Q418 370 452 430L562 621L0 646Z" fill="url(#heroGreen)"/>
  <path d="M1200 146V589L1090 405L1180 258Z" fill="#0a6b35"/>
  <path d="M1022 303L1095 350L1068 432H976L949 350Z" fill="#6fb83f" stroke="#fff" stroke-width="6" stroke-linejoin="round"/>
</svg>
<h1 class="abs display hero-title">Sports Turf<br>Management</h1>
<p class="abs hero-copy">Soccer rugby league softball fields etc from full turf management plans and maintenance to just supply and apply of turf management products</p>
<div class="abs btn-dark hero-btn">Explore More</div>
<div class="abs badge-text"><b>10+</b> years experience</div>
<div class="abs dots"><span></span><span></span><span></span></div>

<div class="abs about-frame"></div>
<div class="abs about-photo" role="img" aria-label="Sports field with stadium stands under a blue sky"></div>
<div class="abs about-square"></div>
<div class="abs turf-roll" role="img" aria-label="Two rolls of fresh turf"></div>
<h2 class="abs display about-title">About Us</h2>
<p class="abs about-copy">Sports turf management is the specialized care of grass surfaces used in athletic and recreational settings. It goes beyond basic lawn care, focusing on durability, playability, and recovery under intense use.</p>
<ul class="abs checks">
  <li><svg width="29" height="29" viewBox="0 0 29 29"><rect width="29" height="29" rx="7" fill="#3f9a3a"/><path d="M8 15l4 4 9-10" fill="none" stroke="#fff" stroke-width="2.2"/></svg><span><b>Fertilization and pest control</b> to promote growth and prevent damage</span></li>
  <li><svg width="29" height="29" viewBox="0 0 29 29"><rect width="29" height="29" rx="7" fill="#3f9a3a"/><path d="M8 15l4 4 9-10" fill="none" stroke="#fff" stroke-width="2.2"/></svg><span><b>Aeration and mowing</b> schedules tailored to<br>seasonal and sport-specific needs</span></li>
  <li><svg width="29" height="29" viewBox="0 0 29 29"><rect width="29" height="29" rx="7" fill="#3f9a3a"/><path d="M8 15l4 4 9-10" fill="none" stroke="#fff" stroke-width="2.2"/></svg><span><b>Irrigation and water management</b> to maintain<br>optimal moisture levels</span></li>
</ul>
<div class="abs btn-dark about-btn">More About</div>

<h2 class="abs display key-title">Key Responsibilities</h2>
<article class="abs card" style="left:156px">
  <div class="card-icon"><svg width="26" height="20" viewBox="0 0 26 20" fill="none" stroke="#fff" stroke-width="2"><path d="M3 19L1 6M8 19L6 2M13 19V4M18 19l2-16M23 19l2-12"/></svg></div>
  <h3>Turfgrass<br>selection</h3>
  <p>based on climate, sport type, and wear tolerance</p>
  <div class="more">More <span class="more-dot"><svg width="9" height="9" viewBox="0 0 9 9" fill="none" stroke="#fff" stroke-width="1.5"><path d="M1 4.5h7M5 1.5l3 3-3 3"/></svg></span></div>
</article>
<article class="abs card" style="left:463px">
  <div class="card-icon"><svg width="30" height="16" viewBox="0 0 30 16" fill="#fff"><path d="M15 1l2.5 5 5.5.8-4 3.9 1 5.3-5-2.6-5 2.6 1-5.3-4-3.9 5.5-.8z"/><path d="M5 4l1.3 2.6 2.7.4-2 1.9.5 2.7L5 10.3 2.5 11.6 3 8.9 1 7l2.7-.4zM25 4l1.3 2.6 2.7.4-2 1.9.5 2.7-2.5-1.3-2.5 1.3.5-2.7-2-1.9 2.7-.4z"/></svg></div>
  <h3>Soil preparation<br>and grading</h3>
  <p>for drainage and root<br>health</p>
  <div class="more">More <span class="more-dot"><svg width="9" height="9" viewBox="0 0 9 9" fill="none" stroke="#fff" stroke-width="1.5"><path d="M1 4.5h7M5 1.5l3 3-3 3"/></svg></span></div>
</article>
<article class="abs card" style="left:769px">
  <div class="card-icon"><svg width="22" height="24" viewBox="0 0 22 24" fill="#fff"><path d="M3 1h2v15H3z"/><path d="M5 2h7v6H5z"/><path d="M8 12h6l5 5-2 2-4-3H8z"/></svg></div>
  <h3>Field marking and<br>layout</h3>
  <p>for compliance with sport regulations</p>
  <div class="more">More <span class="more-dot"><svg width="9" height="9" viewBox="0 0 9 9" fill="none" stroke="#fff" stroke-width="1.5"><path d="M1 4.5h7M5 1.5l3 3-3 3"/></svg></span></div>
</article>

<div class="abs display progress">Inprogress</div>

</body>
</html>
```